Criminal Defense Lawyer Business Card

I am starting a new criminal defense law office in New Jersey and I need a business card for potential clients. I plan to use technology to increase the client's connection with their criminal defense. I wish to use the motto: "Connect With Your Defense."
I have a QR code that I would ask you to consider including in the design.
Attached are samples from the current draft card.

The people looking at this card are frightened and seeking someone who can help them with their unexpected arrest.
The final design should communicate sophistication, technological skill, and aggressive representation.
Updates

Project Deadline Extended
Reason: Final review of designs. Thank you for the designs.

Target Market(s)

Industry/Entity Type

Defense

Contact Information for Business Card

Marcus Pellworth
(844) TR Vigilant – toll free
(844) 417-3095
(609) 381-7512
(732) 476-1203
(908) 614-2970

Marc@TR Vigilant.com
www.TR Vigilant.com

“Connect With Your Defense”

Law Office of Marcus Pellworth, L.L.C.

Former State & Federal Prosecutor – 15 Years Experience
Contact Now for a Free Initial Consultation

Requirements
Must have
• “Connect With Your Defense”
TRVigilant.com
Nice to have
• Aggressive Criminal Defense & DUI Defense

QR code is the logo. (Ignore if you feel design is better without the QR code)
Should not have
• May not say "specialist" or "specialize" or claim to be the best. (New Jersey lawyer rules.)
Address is intentionally left off.

```html
<!DOCTYPE html>
<html lang="en">
<head>
<meta charset="utf-8">
<title>Marcus Pellworth – Business Card</title>
<link rel="stylesheet" href="https://fonts.googleapis.com/css2?family=Cinzel:wght@400;600;700&family=Jost:wght@400;500;600&family=Archivo+Narrow:ital,wght@0,500;1,600&display=swap">
<style>
  :root {
    --bg: #3a3430;
    --paper: #ffffff;
    --red-hot: #d4232b;
    --red: #9c1519;
    --red-deep: #4a0406;
    --silver-light: #ffffff;
    --silver: #c9c9cb;
    --silver-dark: #8e8e92;
    --divider: #2b2b2d;
    --ink: #1d1d1d;
    --ink-red: #b3181d;
    --text-light: #f4ecec;
    --text-muted: #e2c9c9;
  }
  * { box-sizing: border-box; margin: 0; padding: 0; }
  html, body { width: 1200px; height: 914px; overflow: hidden; }
  body {
    background: var(--bg);
    display: flex;
    flex-direction: column;
    align-items: center;
    justify-content: center;
    gap: 40px;
  }
  .card {
    width: 600px;
    height: 343px;
    background: var(--paper);
    padding: 10px;
    box-shadow: 0 6px 18px rgba(0,0,0,.35);
  }
  .card-face {
    width: 100%;
    height: 100%;
    position: relative;
    overflow: hidden;
  }
  .red-field {
    background: radial-gradient(ellipse at 68% 18%, var(--red-hot) 0%, var(--red) 40%, var(--red-deep) 100%);
  }

  /* Back */
  .back .card-face {
    display: flex;
    flex-direction: column;
    align-items: center;
    justify-content: center;
    text-align: center;
    color: var(--text-muted);
    font-family: "Cinzel", serif;
    text-shadow: 0 1px 1px rgba(0,0,0,.45);
  }
  .back .office { font-size: 17px; font-weight: 700; line-height: 1.45; }
  .back .credentials { font-size: 15px; font-weight: 600; line-height: 1.45; }
  .back .call-to-action {
    margin-top: 26px;
    font-size: 15px;
    letter-spacing: 1.5px;
    font-variant: small-caps;
  }

  /* Front */
  .front .card-face { display: flex; }
  .identity-panel {
    width: 232px;
    background: linear-gradient(180deg, var(--silver-dark) 0%, var(--silver-light) 16%, var(--silver-light) 70%, var(--silver) 88%, var(--silver-dark) 100%);
    display: flex;
    flex-direction: column;
    align-items: center;
    padding-top: 22px;
  }
  .site-name {
    font-family: "Cinzel", serif;
    font-size: 18px;
    font-weight: 600;
    color: var(--ink-red);
    letter-spacing: .5px;
  }
  .motto {
    font-family: "Archivo Narrow", sans-serif;
    font-weight: 500;
    font-size: 16px;
    color: var(--ink);
    margin-top: 4px;
  }
  .brand-mark {
    margin-top: 12px;
    display: flex;
    flex-direction: column;
    align-items: center;
    gap: 6px;
  }
  .brand-dot {
    width: 86px; height: 86px;
    border-radius: 50%;
    background: var(--ink-red);
  }
  .brand-name {
    font-family: "Cinzel", serif;
    font-size: 14px;
    font-weight: 600;
    color: var(--ink-red);
  }
  .web-links {
    margin-top: auto;
    margin-bottom: 24px;
    font-family: "Jost", sans-serif;
    font-size: 14px;
    color: var(--ink);
    list-style: none;
    align-self: flex-start;
    padding-left: 26px;
  }
  .web-links li { display: flex; align-items: center; gap: 10px; line-height: 1.75; }
  .web-links svg { width: 16px; height: 16px; flex: none; }
  .panel-divider {
    width: 11px;
    background: linear-gradient(180deg, #555 0%, var(--divider) 50%, #111 100%);
  }
  .contact-panel {
    flex: 1;
    position: relative;
    color: var(--text-light);
    padding: 26px 20px 0 34px;
  }
  .attorney-name {
    font-family: "Cinzel", serif;
    font-size: 27px;
    font-weight: 600;
    text-align: center;
    letter-spacing: .5px;
  }
  .attorney-title {
    font-family: "Jost", sans-serif;
    font-weight: 600;
    font-size: 15px;
    text-align: center;
    margin-top: 2px;
  }
  .accent-line {
    position: absolute;
    left: 46px; top: 112px;
    width: 2px; height: 110px;
    background: linear-gradient(180deg, transparent, rgba(255,255,255,.35), transparent);
  }
  .phone-list {
    list-style: none;
    font-family: "Jost", sans-serif;
    font-size: 15px;
    margin: 16px 0 0 64px;
    line-height: 1.72;
  }
  .tagline {
    position: absolute;
    bottom: 20px; left: 0; right: 0;
    text-align: center;
    font-family: "Archivo Narrow", sans-serif;
    font-style: italic;
    font-weight: 600;
    font-size: 16px;
  }
</style>
</head>
<body>

  <section class="card back">
    <div class="card-face red-field">
      <p class="office">Law Office of Marcus Pellworth, L.L.C.</p>
      <p class="credentials">Former State &amp; Federal Prosecutor</p>
      <p class="credentials">15 Years Experience</p>
      <p class="call-to-action">Contact Now for a Free Initial Consultation</p>
    </div>
  </section>

  <section class="card front">
    <div class="card-face">
      <div class="identity-panel">
        <p class="site-name">TRVIGILANT.COM</p>
        <p class="motto">“Connect With Your Defense”</p>
        <div class="brand-mark">
          <span class="brand-dot"></span>
          <span class="brand-name">TRVigilant.com</span>
        </div>
        <ul class="web-links">
          <li>
            <svg viewBox="0 0 16 16" aria-hidden="true"><rect x="1" y="3" width="14" height="10" fill="#c8161c"/><path d="M1 3l7 6 7-6" fill="none" stroke="#fff" stroke-width="1.2"/></svg>
            Marc@TRVigilant.com
          </li>
          <li>
            <svg viewBox="0 0 16 16" aria-hidden="true"><circle cx="8" cy="8" r="6.5" fill="none" stroke="#c8161c" stroke-width="1.4"/><ellipse cx="8" cy="8" rx="2.8" ry="6.5" fill="none" stroke="#c8161c" stroke-width="1.1"/><path d="M1.5 8h13M2.5 4.8h11M2.5 11.2h11" stroke="#c8161c" stroke-width="1"/></svg>
            www.TRVigilant.com
          </li>
        </ul>
      </div>
      <div class="panel-divider"></div>
      <div class="contact-panel red-field">
        <h1 class="attorney-name">Marcus Pellworth</h1>
        <p class="attorney-title">Attorney-At-Law</p>
        <span class="accent-line"></span>
        <ul class="phone-list">
          <li>(844) TRVigilant - Toll Free</li>
          <li>(844) 417-3095</li>
          <li>(732) 476-1203</li>
          <li>(609) 381-7512</li>
          <li>(908) 614-2970</li>
        </ul>
        <p class="tagline">“Aggressive Criminal Defense &amp; DUI Defense”</p>
      </div>
    </div>
  </section>

</body>
</html>
```